Upmarket building and construction company needs signage

Our building company R Brent Construction, needs signage to put up on the side of our vehicle trailers and on site fencing. We are a building company that specialises in residential construction and carpentry .

I will attach our logo and some inspirational pics for site fencing as well as what our trailer looks like .
Other details i would like on the sign are our
( email) rbrentconstruction@mailbox-example.net
(mobile ) 0493 518 264
(website ) rbrentconstruction. example.net

Target Market(s)

Home owners looking for a reliable local builder who produces good quality work. I have attached some inspirational pics.

Industry/Entity Type

Building and Construction

Colors

Designer to choose colors to be used in the design.

Requirements
Must have
• Our logo, contact information
Nice to have
• We would like the design to have elements of being Elegant, Serious, Modern, Professional, Masculine, Conservative and Upmarket.

```html
<!DOCTYPE html>
<html lang="en">
<head>
<meta charset="UTF-8">
<title>R Brent Construction – Site Signage</title>
<link href="https://fonts.googleapis.com/css2?family=Montserrat:wght@400;500;700;800&display=swap" rel="stylesheet">
<style>
  :root {
    --page-bg: #c9c8c8;
    --sign-bg: #262628;
    --sign-bg-light: #323235;
    --rule: #8a8a8e;
    --text: #ffffff;
    --photo-house-top: #3b3a2a;
    --photo-house-mid: #7a5632;
    --photo-house-low: #4a4a48;
    --photo-finance-dark: #2b3a55;
    --photo-finance-glow: #d88a45;
  }
  * { margin: 0; padding: 0; box-sizing: border-box; }
  html, body {
    width: 900px;
    height: 1200px;
    overflow: hidden;
    background: var(--page-bg);
    font-family: "Montserrat", sans-serif;
  }
  .canvas {
    position: relative;
    width: 900px;
    height: 1200px;
  }
  .sign {
    position: absolute;
    left: 56px;
    top: 452px;
    width: 788px;
    height: 295px;
    background: radial-gradient(ellipse at 50% 40%, var(--sign-bg-light) 0%, var(--sign-bg) 70%);
    overflow: hidden;
    color: var(--text);
  }
  .sign__rules {
    position: absolute;
    inset: 0;
  }
  .photo {
    position: absolute;
    top: 40px;
    width: 239px;
    height: 223px;
  }
  .photo--house {
    left: 23px;
    background: linear-gradient(180deg, var(--photo-house-top) 0%, #2f3a25 30%, var(--photo-house-mid) 55%, #a86a35 68%, var(--photo-house-low) 85%, #3e4a2c 100%);
  }
  .photo--finance {
    left: 533px;
    background: radial-gradient(circle at 52% 60%, #f3c07a 0%, var(--photo-finance-glow) 18%, #6a4a3a 45%, var(--photo-finance-dark) 100%);
  }
  .brand {
    position: absolute;
    left: 300px;
    top: 26px;
    display: flex;
    align-items: center;
    gap: 5px;
  }
  .brand__mark {
    width: 9px;
    height: 9px;
    background: var(--text);
  }
  .brand__name {
    font-size: 7.5px;
    font-weight: 500;
    letter-spacing: 0.6px;
    line-height: 1.25;
    text-transform: uppercase;
  }
  .headline {
    position: absolute;
    left: 300px;
    width: 210px;
    top: 90px;
    text-align: center;
  }
  .headline__main {
    font-size: 35px;
    font-weight: 700;
    letter-spacing: 1.5px;
    line-height: 1;
  }
  .headline__sub {
    font-size: 16px;
    font-weight: 400;
    margin-top: 3px;
    padding-left: 24px;
  }
  .contact {
    position: absolute;
    left: 322px;
    top: 206px;
    list-style: none;
    font-size: 8.6px;
    font-weight: 400;
  }
  .contact__item {
    display: flex;
    align-items: center;
    gap: 6px;
    height: 16.5px;
  }
  .contact__bullet {
    width: 6px;
    height: 6px;
    background: var(--text);
    flex: none;
  }
</style>
</head>
<body>
<div class="canvas">
  <section class="sign">
    <svg class="sign__rules" width="788" height="295" viewBox="0 0 788 295" fill="none" stroke="var(--rule)" stroke-width="0.8">
      <polyline points="0,19 294,19 294,70"/>
      <polyline points="262,148 302,148 302,295"/>
      <line x1="504" y1="0" x2="504" y2="295"/>
      <line x1="504" y1="141" x2="533" y2="141"/>
      <line x1="522" y1="85" x2="533" y2="85"/>
      <polyline points="522,85 522,295"/>
      <line x1="772" y1="85" x2="788" y2="85"/>
      <line x1="0" y1="236" x2="23" y2="236"/>
    </svg>

    <div class="photo photo--house" role="img" aria-label="Photograph of a lit modern timber and stone home at dusk against a forested hillside"></div>
    <div class="photo photo--finance" role="img" aria-label="Photograph of hands around stacked coins with a glowing house and building icon overlay"></div>

    <div class="brand">
      <span class="brand__mark"></span>
      <span class="brand__name">R Brent<br>Construction</span>
    </div>

    <div class="headline">
      <h1 class="headline__main">QUALITY</h1>
      <p class="headline__sub">craftsmanship</p>
    </div>

    <ul class="contact">
      <li class="contact__item"><span class="contact__bullet"></span>0493 518 264</li>
      <li class="contact__item"><span class="contact__bullet"></span>rbrentconstruction@mailbox-example.net</li>
      <li class="contact__item"><span class="contact__bullet"></span>rbrentconstruction@mailbox-example.net</li>
    </ul>
  </section>
</div>
</body>
</html>
```